Aged Care Consultancy Business needs a business card design

I need a two sided business card - I want it clean and professional. Surprise me

Target Market(s)

middle aged and ageing victorians

Industry/Entity Type

Health Care

Contact Information for Business Card

Text to be included

Logo
Aged Care Consulting Services
Professional, Reliable, Affordable

Tovan Brelsick
Director
0427 31 64 92 (larger)
1300 73 29 41
tovan@wadolire.com.au
www.wadolcare.com.au
Linkfolk (details TBA)

include little icons beside the contact info:

- Envelope = email
- Phone = phone
- Globe = website

Font styles to use
Serif
Sans Serif

Requirements
Must have
• look proffesional and clean

```html
<!DOCTYPE html>
<html lang="en">
<head>
<meta charset="utf-8">
<title>Wadol Care – Business Card</title>
<link rel="stylesheet" href="https://fonts.googleapis.com/css2?family=Open+Sans:wght@400;600;700&display=swap">
<style>
  :root {
    --stage: #e4e8ea;
    --card-white: #ffffff;
    --card-black: #1a1a1a;
    --card-black-edge: #232323;
    --brand-blue: #2f4f98;
    --brand-orange: #eb9a35;
    --text-light: #f2f2f2;
    --shadow: rgba(0, 0, 0, 0.22);
  }
  * { box-sizing: border-box; margin: 0; padding: 0; }
  html, body { width: 1200px; height: 960px; overflow: hidden; }
  body {
    background: var(--stage);
    font-family: "Open Sans", sans-serif;
    display: flex;
    flex-direction: column;
    align-items: center;
    justify-content: center;
    gap: 60px;
  }
  .card {
    width: 700px;
    height: 400px;
    border-radius: 4px;
    box-shadow: 0 14px 34px var(--shadow);
    position: relative;
  }
  .card--front {
    background: var(--card-white);
    display: flex;
    align-items: center;
    justify-content: center;
  }
  .brand-name {
    font-family: "Open Sans", sans-serif;
    font-weight: 700;
    color: var(--brand-blue);
    letter-spacing: 0.5px;
    display: flex;
    align-items: center;
    gap: 18px;
  }
  .brand-name__dot {
    display: block;
    border-radius: 50%;
    background: var(--brand-orange);
  }
  .card--front .brand-name { font-size: 64px; }
  .card--front .brand-name__dot { width: 40px; height: 40px; }

  .card--back {
    background: linear-gradient(90deg, var(--card-black) 0%, var(--card-black) 62%, var(--card-black-edge) 100%);
    color: var(--text-light);
    padding: 36px 44px;
  }
  .person {
    border-left: 6px solid var(--brand-blue);
    padding-left: 18px;
  }
  .person__name { font-size: 26px; font-weight: 600; letter-spacing: 1px; line-height: 1.1; }
  .person__role { font-size: 15px; color: var(--brand-blue); letter-spacing: 0.5px; }
  .card--back .brand-name {
    position: absolute;
    top: 40px;
    right: 44px;
    font-size: 30px;
    gap: 10px;
  }
  .card--back .brand-name__dot { width: 20px; height: 20px; }

  .contacts {
    list-style: none;
    position: absolute;
    left: 64px;
    bottom: 40px;
    display: flex;
    flex-direction: column;
    gap: 8px;
  }
  .contacts__item {
    display: flex;
    align-items: center;
    gap: 16px;
    font-size: 17px;
    letter-spacing: 0.6px;
  }
  .contacts__item--primary { font-size: 21px; font-weight: 600; }
  .contacts__icon { width: 18px; height: 18px; flex: none; }
  .contacts__icon * { stroke: var(--brand-orange); fill: none; stroke-width: 1.8; }
  .contacts__icon .solid { fill: var(--brand-orange); stroke: none; }
</style>
</head>
<body>
  <section class="card card--front" aria-label="Card front">
    <div class="brand-name"><span class="brand-name__dot"></span>wadol care</div>
  </section>

  <section class="card card--back" aria-label="Card back">
    <div class="person">
      <p class="person__name">Tovan Brelsick</p>
      <p class="person__role">Director</p>
    </div>
    <div class="brand-name"><span class="brand-name__dot"></span>wadol care</div>

    <ul class="contacts">
      <li class="contacts__item contacts__item--primary">
        <svg class="contacts__icon" viewBox="0 0 18 18"><path class="solid" d="M2 6c0-2 3-3 7-3s7 1 7 3v2h-4V6.5H6V8H2z"/><rect class="solid" x="3" y="9" width="12" height="7" rx="1"/></svg>
        0427 31 64 92
      </li>
      <li class="contacts__item">
        <svg class="contacts__icon" viewBox="0 0 18 18"><rect x="5" y="2" width="8" height="14" rx="1.5"/><line x1="8" y1="13.5" x2="10" y2="13.5"/></svg>
        1300 73 29 41
      </li>
      <li class="contacts__item">
        <svg class="contacts__icon" viewBox="0 0 18 18"><rect x="2" y="4" width="14" height="10" rx="1"/><polyline points="2,4 9,10 16,4"/></svg>
        tovan@wadolire.com.au
      </li>
      <li class="contacts__item">
        <svg class="contacts__icon" viewBox="0 0 18 18"><circle cx="9" cy="9" r="7"/><ellipse cx="9" cy="9" rx="3" ry="7"/><line x1="2" y1="9" x2="16" y2="9"/></svg>
        www.wadolcare.com.au
      </li>
      <li class="contacts__item">
        <svg class="contacts__icon" viewBox="0 0 18 18"><rect class="solid" x="3" y="3" width="12" height="12" rx="2"/></svg>
        Linkfolk (details TBA)
      </li>
    </ul>
  </section>
</body>
</html>
```